Business Card Design Project

This is to go hand in hand with our stationery project.
Target Market(s)
Business Professionals in the Finance, HR and C-Level management arena. They are global companies that run enterprise technology solutions/products.
Mostly Male, mid 30's to 60's.
Industry/Entity Type
Business
Font styles to use
Other font styles liked:
- Calibri
Colors
9bcb3c
000000
1b1b1b
c4c4c4
ffffff
Requirements
Must have
- Logo
Name, title, contact details, address on the front of the card.
ABN and web address need to be on the card, along with our tag line
See | Share | Do
We also require rounded corners and for the card to be landscape please.
Our green is
C98 M0 Y93 K0
Modern, contemporary and must have white space for people to write on.
Nice to have
- Consistent elements with the stationery design.
Should not have
- No 90's waves - We want the feeling of movement but no wavey lines.

```html
<!DOCTYPE html>
<html lang="en">
<head>
<meta charset="utf-8">
<title>KLV Business Solutions – Business Card Proof</title>
<link rel="stylesheet" href="https://fonts.googleapis.com/css2?family=Carlito:wght@400;700&display=swap">
<style>
  :root {
    --brand-green: #9bcb3c;
    --green-deep: #5f9626;
    --green-light: #b9dc5c;
    --heading-green: #55862c;
    --band-dark: #2b2b2b;
    --band-mid: #4a4a4a;
    --ink: #000000;
    --near-black: #1b1b1b;
    --muted: #6d6d6d;
    --silver: #c4c4c4;
    --white: #ffffff;
    --font-body: "Carlito", "Calibri", Arial, sans-serif;
  }
  * { box-sizing: border-box; margin: 0; padding: 0; }
  html, body {
    width: 1200px;
    height: 513px;
    overflow: hidden;
    background: var(--white);
    font-family: var(--font-body);
  }
  .proof-sheet {
    position: relative;
    width: 1200px;
    height: 513px;
  }
  .proof-title {
    position: absolute;
    top: 14px;
    left: 0;
    width: 100%;
    text-align: center;
    font-size: 36px;
    font-weight: 400;
    color: var(--heading-green);
  }
  .side-label {
    position: absolute;
    top: 86px;
    width: 460px;
    text-align: center;
    font-size: 17px;
    color: var(--heading-green);
  }
  .side-label--front { left: 60px; }
  .side-label--back { left: 672px; }

  .card {
    position: absolute;
    top: 126px;
    width: 460px;
    height: 270px;
    overflow: hidden;
    border: 1px solid var(--silver);
  }
  .card--front { left: 60px; }
  .card--back { left: 672px; }

  .map-backdrop {
    position: absolute;
    inset: 0;
    background:
      radial-gradient(ellipse at 30% 40%, var(--green-light) 0%, transparent 55%),
      radial-gradient(ellipse at 75% 70%, var(--green-deep) 0%, transparent 60%),
      linear-gradient(135deg, var(--green-deep) 0%, var(--brand-green) 50%, var(--green-light) 100%);
  }

  /* Front */
  .front-header {
    position: absolute;
    top: 0; left: 0;
    width: 100%;
    height: 92px;
    background: var(--band-dark);
  }
  .front-logo-block {
    position: absolute;
    top: 0; left: 0;
    width: 142px;
    height: 92px;
    background: var(--band-mid);
    display: flex;
    align-items: center;
    justify-content: center;
    text-align: center;
  }
  .brand-name {
    color: var(--white);
    font-weight: 700;
    font-size: 15px;
    line-height: 1.15;
  }
  .front-company {
    position: absolute;
    top: 24px;
    right: 18px;
    text-align: right;
  }
  .company-name {
    color: var(--brand-green);
    font-weight: 700;
    font-size: 24px;
    line-height: 1;
  }
  .company-sub {
    color: var(--white);
    font-size: 14px;
    margin-top: 6px;
  }
  .front-contact {
    position: absolute;
    top: 140px;
    left: 30px;
    width: 404px;
    text-align: center;
    color: var(--near-black);
    font-style: normal;
    font-weight: 700;
    font-size: 15px;
    line-height: 23px;
  }
  .front-footer {
    position: absolute;
    left: 0; bottom: 0;
    width: 100%;
    height: 52px;
    background: var(--band-dark);
  }
  .abn {
    position: absolute;
    left: 10px;
    bottom: 9px;
    font-size: 12px;
    color: var(--muted);
  }
  .tagline {
    position: absolute;
    right: 12px;
    top: 7px;
    color: var(--white);
    font-size: 18px;
  }
  .web {
    position: absolute;
    right: 12px;
    bottom: 7px;
    color: var(--white);
    font-size: 12px;
    font-weight: 700;
  }

  /* Back */
  .back-header {
    position: absolute;
    top: 0; left: 0;
    width: 100%;
    height: 52px;
    background: var(--band-dark);
    display: flex;
    align-items: center;
    justify-content: center;
  }
  .back-header .company-name { font-size: 26px; }
  .back-logo {
    position: absolute;
    top: 96px;
    left: 160px;
    width: 140px;
    height: 86px;
    display: flex;
    align-items: center;
    justify-content: center;
    text-align: center;
  }
  .back-logo .brand-name { font-size: 17px; }
  .back-footer {
    position: absolute;
    left: 0; bottom: 0;
    width: 100%;
    height: 42px;
    background: var(--band-dark);
    display: flex;
    align-items: center;
    justify-content: center;
    color: var(--white);
    font-size: 18px;
  }
</style>
</head>
<body>
<main class="proof-sheet">
  <h1 class="proof-title">For Proof</h1>
  <p class="side-label side-label--front">Front Side</p>
  <p class="side-label side-label--back">Back Side</p>

  <section class="card card--front" aria-label="Business card front">
    <div class="map-backdrop" role="img" aria-label="Green world map backdrop"></div>
    <header class="front-header">
      <div class="front-logo-block">
        <span class="brand-name">KLV<br>Business Solutions</span>
      </div>
      <div class="front-company">
        <p class="company-name">KLV Business Solutions</p>
        <p class="company-sub">KLV Business Solutions Rebrand Brief</p>
      </div>
    </header>
    <address class="front-contact">
      T: +61 29555 0147 • F: +61 29555 0148<br>
      Level 7, 42 Ferry Street, Eastwick&nbsp; NSW 2061
    </address>
    <footer class="front-footer">
      <span class="abn">ABN: 12 345 678 901</span>
      <span class="tagline">Plan • Build •Grow</span>
      <span class="web">www.klvbusiness.com</span>
    </footer>
  </section>

  <section class="card card--back" aria-label="Business card back">
    <div class="map-backdrop" role="img" aria-label="Green world map backdrop"></div>
    <header class="back-header">
      <p class="company-name">KLV Business Solutions</p>
    </header>
    <div class="back-logo">
      <span class="brand-name">KLV<br>Business Solutions</span>
    </div>
    <footer class="back-footer">KLV Business Solutions Rebrand Brief</footer>
  </section>
</main>
</body>
</html>
```